VelloPath Business Card

Our company is called VelloPath and we are based in Tel Aviv, Israel. We create innovative and exciting methods for getting people on the web engaged with content. We need a cool yet professional business card that will represent our management level employees. keep in mind this is a start up company with a young atmosphere. You can be inspired by our logo (file attached, make sure you have the right font "Ubuntu-Condensed") Use the colors that are used in the logo and create a colourful and professional business card.

```html
<!DOCTYPE html>
<html lang="en">
<head>
<meta charset="utf-8">
<title>VelloPath Business Card</title>
<link href="https://fonts.googleapis.com/css2?family=Ubuntu:wght@400;500&family=Ubuntu+Condensed&display=swap" rel="stylesheet">
<style>
  :root {
    --bg: #2b2b2d;
    --card: #ffffff;
    --ink: #1d1d1f;
    --ink-soft: #3a3a3c;
    --blue: #3fa9d6;
    --pink: #e2227a;
    --green: #7cbd3a;
    --yellow: #f8c81c;
    --orange: #f2a33a;
    --purple: #8e2a8c;
  }
  * { box-sizing: border-box; margin: 0; padding: 0; }
  html, body { width: 1200px; height: 900px; overflow: hidden; }
  body {
    background: var(--bg);
    font-family: "Ubuntu", sans-serif;
    color: var(--ink);
    display: flex;
    flex-direction: column;
    align-items: center;
    justify-content: center;
    gap: 40px;
  }
  .card {
    position: relative;
    width: 700px;
    height: 400px;
    background: var(--card);
    overflow: hidden;
  }

  /* Back side */
  .back-pattern {
    position: absolute;
    left: 0; top: 0;
    width: 100%; height: 270px;
    background: linear-gradient(100deg,
      rgba(63,169,214,.55) 0%,
      rgba(248,200,28,.55) 22%,
      rgba(226,34,122,.45) 42%,
      rgba(124,189,58,.45) 62%,
      rgba(142,42,140,.4) 80%,
      rgba(242,163,58,.45) 100%);
    -webkit-mask-image: linear-gradient(to bottom, #000 55%, transparent 100%);
            mask-image: linear-gradient(to bottom, #000 55%, transparent 100%);
  }
  .back .brand {
    position: absolute;
    right: 42px;
    bottom: 54px;
  }

  /* Brand name */
  .brand {
    display: flex;
    align-items: center;
    gap: 10px;
    font-family: "Ubuntu Condensed", sans-serif;
    font-size: 40px;
    color: var(--ink);
    letter-spacing: .5px;
  }
  .brand-dot {
    width: 22px; height: 22px;
    border-radius: 50%;
    background: var(--blue);
  }

  /* Front side */
  .front-pattern {
    position: absolute;
    left: 20px; top: 40px;
    width: 430px; height: 250px;
    border-radius: 50%;
    background: radial-gradient(ellipse at center,
      rgba(226,34,122,.12) 0%,
      rgba(63,169,214,.10) 40%,
      rgba(124,189,58,.08) 65%,
      transparent 80%);
  }
  .front .brand {
    position: absolute;
    right: 42px;
    top: 78px;
    font-size: 52px;
  }
  .person {
    position: absolute;
    left: 44px;
    top: 112px;
  }
  .person-name {
    font-size: 21px;
    font-weight: 500;
  }
  .person-role {
    font-size: 13px;
    color: var(--ink-soft);
    margin-top: 4px;
  }
  .address {
    position: absolute;
    right: 42px;
    top: 190px;
    text-align: right;
    font-size: 14px;
    line-height: 1.55;
    color: var(--ink-soft);
  }
  .contacts {
    position: absolute;
    left: 44px;
    bottom: 40px;
    list-style: none;
    display: flex;
    flex-direction: column;
    gap: 8px;
  }
  .contact {
    display: flex;
    align-items: center;
    gap: 12px;
    font-size: 16px;
  }
  .contact-icon {
    width: 24px; height: 24px;
    border-radius: 50%;
    display: flex;
    align-items: center;
    justify-content: center;
  }
  .contact-icon.phone { background: var(--pink); }
  .contact-icon.mail { background: var(--green); }
  .contact-icon.web { background: var(--blue); }
</style>
</head>
<body>

  <section class="card back" aria-label="Business card, back">
    <div class="back-pattern" role="img" aria-label="Colourful scattered dots pattern in pink, yellow, blue, green, purple and orange"></div>
    <div class="brand"><span class="brand-dot"></span>VelloPath</div>
  </section>

  <section class="card front" aria-label="Business card, front">
    <div class="front-pattern" role="img" aria-label="Faint pastel scattered dots pattern"></div>

    <div class="person">
      <p class="person-name">Noa Levran</p>
      <p class="person-role">Founder &amp; CEO</p>
    </div>

    <div class="brand"><span class="brand-dot"></span>VelloPath</div>

    <address class="address" style="font-style:normal">
      87 Maple Grove Street<br>
      Tel Aviv, Israel<br>
      61400
    </address>

    <ul class="contacts">
      <li class="contact">
        <span class="contact-icon phone">
          <svg width="12" height="14" viewBox="0 0 12 14"><rect x="2" y="1" width="8" height="12" rx="1.5" fill="none" stroke="#fff" stroke-width="1.5"/><circle cx="6" cy="10.5" r="0.9" fill="#fff"/></svg>
        </span>
        +972 500 318 642
      </li>
      <li class="contact">
        <span class="contact-icon mail">
          <svg width="14" height="10" viewBox="0 0 14 10"><rect x="1" y="1" width="12" height="8" rx="1" fill="none" stroke="#fff" stroke-width="1.4"/><path d="M1 1.5 7 6 13 1.5" fill="none" stroke="#fff" stroke-width="1.4"/></svg>
        </span>
        noa@vellopath.com
      </li>
      <li class="contact">
        <span class="contact-icon web">
          <svg width="14" height="14" viewBox="0 0 14 14"><g fill="none" stroke="#fff" stroke-width="1.2"><circle cx="7" cy="7" r="5.5"/><ellipse cx="7" cy="7" rx="2.4" ry="5.5"/><path d="M1.5 7h11M2.5 4h9M2.5 10h9"/></g></svg>
        </span>
        www.vellopath.com
      </li>
    </ul>
  </section>

</body>
</html>
```